4x6 Postcard Design Full Color Double Sided

Hello, I am in need of a postcard design. The document with details is attached. And I am writing here also:

To My Dear Colleague,

This week, I want you to do yourself and me a favor, okay?

I want you to ask your boss for a $100,000 per year salary increase. If the answer is no then I want you to “give yourself” a

$10,000 per month pay increase RIGHT NOW!

The opportunity to make 6-7 figures using SIMPLE online systems is exploding right before your eyes. Why aren’t you paying attention? Is It because you don’t have any idea how to earn money online? Or are you intimidated by the thought of it because you’re not tech-savvy?

Throw any negative thoughts out of your mind and let us help you build a $100,000 + yearly income that runs on automatic. We’re not promising a million dollars overnight or that you’ll be able to quit your job tomorrow, BUT if an extra $10,000 per month would help you reach your goals, then you should take action today!

OUR SIMPLE IS SO EASY TO USE, A FIFTH GRADER COULD BE SUCCESSFUL!

We’re so sure you will be successful with our system that we are inviting you to
GET STARTED TODAY FOR FREE!!!

That’s right…for FREE! No credit card is required.

GO SIGN UP NOW:
www.qmvhub.com/joinFREE
Enter Referral ID#

KV-R8057

Free offer expires in 48 hours!!!

Instructions for designers:
I’d like the color scheme to stay consistent with my company’s color scheme. To see the color scheme of Blue Lark Gains go to www.qmvhub.com
As you are reading the text, please make certain parts of the text be emphasized on the postcard – wherever you feel necessary. When you read it, what would catch your attention? Those parts are the parts I’d like you to emphasize on the card by making them bolder, or a different color, or larger or highlighted.

The postcard is a 4x6 card, double-sided, full color

The text above is for the front side. The back will be the same thing, except in the spot where I have KV-R8057. On the backside it should say: (Use ID# on reverse side)

It’s like you are really only designing a one-sided card because the back side is almost an exact duplicate.

Thank you, you rock! =)

Target Market(s)

work from home seekers / make money online enthusiasts

Font styles to use
Serif

Requirements
Must have
• Color scheme similar to the color scheme at www.qmvhub.com
• The rest of the requirements are attached to the word doc.
• I will also send the logo, but it wouldn't let me upload because the file is too large.
Nice to have
• I really I am looking for something that really looks clean, but attention-grabbing

```html
<!DOCTYPE html>
<html lang="en">
<head>
<meta charset="utf-8">
<title>Blue Lark Gains – Postcard</title>
<link href="https://fonts.googleapis.com/css2?family=Raleway:wght@400;500;600;700&display=swap" rel="stylesheet">
<style>
  :root {
    --sky-top: #f4f8fb;
    --sky-mid: #e4f0f8;
    --sky-low: #cde3f2;
    --ink: #1f1f1f;
    --brand-grey: #6a6a6a;
    --brand-blue: #4fb4e3;
    --art-light: rgba(250, 252, 253, 0.95);
    --art-mid: rgba(214, 226, 236, 0.7);
    --art-fade: rgba(205, 227, 242, 0);
  }
  * { margin: 0; padding: 0; box-sizing: border-box; }
  html, body { width: 800px; height: 1200px; overflow: hidden; }
  body {
    font-family: "Raleway", sans-serif;
    color: var(--ink);
    background: #ffffff;
  }
  .postcard {
    position: relative;
    width: 800px;
    height: 1200px;
    overflow: hidden;
    background: linear-gradient(180deg, var(--sky-top) 0%, var(--sky-mid) 45%, var(--sky-low) 100%);
  }
  .summit-art {
    position: absolute;
    left: 420px; top: 680px;
    width: 380px; height: 520px;
    background: radial-gradient(ellipse 70% 65% at 62% 72%, var(--art-light) 0%, var(--art-mid) 45%, var(--art-fade) 100%);
  }
  .block { position: absolute; left: 48px; }
  .brand {
    position: absolute; top: 56px; left: 424px;
    display: flex; align-items: center; gap: 14px;
  }
  .brand-dot { width: 26px; height: 26px; border-radius: 50%; background: var(--brand-blue); }
  .brand-name { font-size: 36px; font-weight: 600; color: var(--brand-grey); }
  .salutation { top: 80px; font-size: 24px; font-weight: 500; }
  .body-text { font-size: 20px; line-height: 26.6px; font-weight: 400; }
  .intro { top: 143px; width: 350px; }
  .ask { top: 225px; width: 712px; }
  .pay-raise { top: 307px; font-size: 24px; font-weight: 600; }
  .opportunity { top: 365px; width: 712px; }
  .reassure { top: 480px; width: 716px; }
  .easy { top: 658px; width: 640px; font-size: 23px; font-weight: 600; letter-spacing: 0.6px; line-height: 30px; text-transform: uppercase; }
  .invite { top: 748px; width: 384px; }
  .free-start { top: 831px; font-size: 23px; font-weight: 600; letter-spacing: 0.4px; }
  .no-card { top: 887px; }
  .signup { top: 969px; }
  .referral-label { top: 1050px; font-size: 21.5px; font-weight: 500; }
  .referral-id { top: 1085px; font-size: 31px; font-weight: 500; letter-spacing: 1px; }
  .expiry { top: 1133px; font-size: 17px; font-weight: 500; }
</style>
</head>
<body>
<main class="postcard">
  <div class="summit-art" role="img" aria-label="Illustration of a businessman standing on a snowy mountain peak holding up a glowing light bulb"></div>

  <div class="brand">
    <span class="brand-dot"></span>
    <span class="brand-name">Blue Lark Gains</span>
  </div>

  <h1 class="block salutation">To My Dear Colleague,</h1>

  <p class="block body-text intro">This week, I want you to do yourself and me a favor, okay?</p>

  <p class="block body-text ask">I want you to ask your boss for a $100,000 per year salary increase. If the answer is no then I want you to “give yourself” a</p>

  <p class="block pay-raise">$10,000 per month pay increase RIGHT NOW!</p>

  <p class="block body-text opportunity">The opportunity to make 6-7 figures using SIMPLE online systems is exploding right before your eyes. Why aren’t you paying attention? Is It because you don’t have any idea how to earn money online?&nbsp; Or are you intimidated by the thought of it because you’re not tech-savvy?</p>

  <p class="block body-text reassure">Throw any negative thoughts out of your mind and let us help you build a $100,000 + yearly income that runs on automatic. We’re not promising a million dollars overnight or that you’ll be able to quit your job tomorrow, BUT if an extra $10,000 per month would help you reach your goals, then you should take action today!</p>

  <h2 class="block easy">Our simple is so easy to use, a fifth grader could be successful!</h2>

  <p class="block body-text invite">We’re so sure you will be successful with our system that we are inviting you to</p>

  <p class="block free-start">GET STARTED TODAY FOR FREE!!!</p>

  <p class="block body-text no-card">That’s right…for FREE!<br>No credit card is required.</p>

  <p class="block body-text signup">GO SIGN UP NOW:<br>www.qmvhub.com/joinFREE</p>

  <p class="block referral-label">Enter Referral ID#</p>
  <p class="block referral-id">KV-R8057</p>
  <p class="block expiry">Free offer expires in 48 hours!!!</p>
</main>
</body>
</html>
```